Modern Spot UV Business Card design

We are a relatively new real estate agency. We need a business card that reflects the professionalism and prestige of our company but is also modern and fresh, based around our logo.
We would love to utilise spot UV.
Happy to let the designers use their imagination and see what they come up with (we're not very creative, so have no ideas for you, sorry) :-)
We'd like one for each staff member, but I've just provided one staff members photo here to avoid confusion.

Target Market(s)

Families

Industry/Entity Type

Real Estate Agent

Contact Information for Business Card

Dale Verco - Director & Principal
Mobile: 0491 627 540
Email: dale.verco@vbrokers.example.au
Phone: (08) 8374 6150
Fax: (08) 8374 6198
www.vercobrokersproperty.example.au

Font styles to use
Other font styles liked:
• Kabel Dm BT

Requirements
Must have
• Contact details, logo, photo, spot UV
Nice to have
• Modern interesting features that will make people comment. Nothing too feminine nor too masculine.
Should not have
• No houses! Nothing typical of a real estate agent.

```html
<!DOCTYPE html>
<html lang="en">
<head>
<meta charset="utf-8">
<title>Verco Brokers – Business Card</title>
<link rel="stylesheet" href="https://fonts.googleapis.com/css2?family=Open+Sans:ital,wght@0,400;0,600;0,700;1,700&display=swap">
<style>
  :root{
    --stage:#34444e;
    --card:#ffffff;
    --ink:#1f1f1f;
    --band:#1e1d1d;
    --orange:#f7931e;
    --blue:#1a8fd6;
    --yellow:#ffd21f;
    --photo-light:#f2f3f4;
    --photo-mid:#c9ccd0;
    --photo-dark:#4c5157;
  }
  *{box-sizing:border-box;margin:0;padding:0}
  html,body{width:1200px;height:1000px;overflow:hidden}
  body{background:var(--stage);font-family:"Open Sans",Arial,sans-serif;color:var(--ink);position:relative}

  .card{position:absolute;left:260px;width:680px;height:390px;background:var(--card);overflow:hidden;box-shadow:0 18px 40px rgba(0,0,0,.35)}
  .card--front{top:80px}
  .card--back{top:530px}

  .brand{display:flex;align-items:center;gap:10px;font-weight:700;color:var(--ink);letter-spacing:-.5px;white-space:nowrap}
  .brand__dot{width:16px;height:16px;border-radius:50%;background:var(--orange);flex:none}

  .dashes{display:flex;gap:20px}
  .dashes span{display:block;width:36px;height:5px}
  .dashes .d1{background:var(--orange)}
  .dashes .d2{background:var(--blue)}
  .dashes .d3{background:var(--yellow)}

  /* front */
  .front__brand{position:absolute;top:100px;left:0;right:0;justify-content:center;font-size:40px}
  .front__dashes{position:absolute;top:180px;left:0;right:0;justify-content:center}
  .front__band{position:absolute;left:0;right:0;bottom:0;height:82px;background:var(--band);display:flex;align-items:center;justify-content:center;gap:12px;color:#fff;font-weight:600;font-size:19px;letter-spacing:.6px}

  /* back */
  .back__photo{position:absolute;left:0;top:0;width:262px;height:390px;background:linear-gradient(180deg,var(--photo-light) 0%,var(--photo-light) 35%,var(--photo-mid) 60%,var(--photo-dark) 100%)}
  .back__divider{position:absolute;left:262px;top:0;width:7px;height:390px;background:linear-gradient(90deg,#dcdcdc,#f7f7f7)}
  .nameplate{position:absolute;left:0;bottom:0;width:262px}
  .nameplate__name{display:inline-block;background:rgba(60,60,60,.75);padding:4px 28px 4px 24px;font-size:24px;font-weight:700;font-style:italic;letter-spacing:1px;white-space:nowrap}
  .nameplate__first{color:var(--blue)}
  .nameplate__last{color:var(--orange)}
  .nameplate__title{background:rgba(30,30,30,.85);color:#fff;font-weight:700;font-size:15px;padding:6px 24px 8px;white-space:nowrap}

  .contacts{position:absolute;left:294px;top:26px;list-style:none}
  .contacts li{display:flex;align-items:center;gap:20px;height:33px;font-size:17px;color:var(--ink);white-space:nowrap}
  .contacts svg{width:24px;height:22px;flex:none;fill:var(--blue)}
  .back__dashes{position:absolute;top:208px;left:388px}
  .back__brand{position:absolute;top:262px;left:338px;font-size:34px}
</style>
</head>
<body>

<section class="card card--front">
  <div class="brand front__brand"><span class="brand__dot"></span>Verco Brokers</div>
  <div class="dashes front__dashes"><span class="d1"></span><span class="d2"></span><span class="d3"></span></div>
  <div class="front__band">
    <svg width="24" height="24" viewBox="0 0 24 24" fill="none" stroke="#fff" stroke-width="1.6" aria-hidden="true">
      <circle cx="12" cy="12" r="10"/><ellipse cx="12" cy="12" rx="4.5" ry="10"/><path d="M2 12h20M4 7h16M4 17h16"/>
    </svg>
    <span>www.vercobrokersproperty.example.au</span>
  </div>
</section>

<section class="card card--back">
  <div class="back__photo" role="img" aria-label="Portrait photo of Dale Verco, smiling, in a grey suit and striped shirt"></div>
  <div class="back__divider"></div>
  <div class="nameplate">
    <div class="nameplate__name"><span class="nameplate__first">Dale</span> <span class="nameplate__last">Verco</span></div>
    <div class="nameplate__title">Director &amp; Principal</div>
  </div>

  <ul class="contacts">
    <li><svg viewBox="0 0 24 24" aria-label="Mobile"><path d="M7 1h10a2 2 0 0 1 2 2v18a2 2 0 0 1-2 2H7a2 2 0 0 1-2-2V3a2 2 0 0 1 2-2zm0 3v15h10V4zm5 16.2a1 1 0 1 0 0 .01z"/></svg>0491 627 540</li>
    <li><svg viewBox="0 0 24 24" aria-label="Phone"><path d="M6.6 10.8a15 15 0 0 0 6.6 6.6l2.2-2.2a1 1 0 0 1 1-.25 11.4 11.4 0 0 0 3.6.6 1 1 0 0 1 1 1V20a1 1 0 0 1-1 1A17 17 0 0 1 3 4a1 1 0 0 1 1-1h3.5a1 1 0 0 1 1 1c0 1.25.2 2.45.6 3.6a1 1 0 0 1-.25 1z"/></svg>(08) 8374 6150</li>
    <li><svg viewBox="0 0 24 24" aria-label="Email"><path d="M2 5h20v14H2zm2 2v.5l8 5.5 8-5.5V7zm0 3v7h16v-7l-8 5.5z"/></svg>dale.verco@vbrokers.example.au</li>
    <li><svg viewBox="0 0 24 24" aria-label="Fax"><path d="M7 2h9l3 3v5H7zM2 9h4v13H2zm5 2h15v11H7zm3 3v2h2v-2zm4 0v2h2v-2zm4 0v2h2v-2zm-8 4v2h2v-2zm4 0v2h2v-2zm4 0v2h2v-2z"/></svg>(08) 8374 6198</li>
  </ul>

  <div class="dashes back__dashes"><span class="d1"></span><span class="d2"></span><span class="d3"></span></div>
  <div class="brand back__brand"><span class="brand__dot"></span>Verco Brokers</div>
</section>

</body>
</html>
```